webpage design for www.lumivaleYOU.com

Hi-
I am creating a website about weight loss through healthy eating. The target audience is 80% women, of all races and ethnic backgrounds, in the 35-55 age range, all of whom are overweight and want to lose weight.
At first (which is where you come in), the website will be strictly informational, and products for sale will be added later.
Obviously not all of the following information can be incorporated into the design, but to give you some background, here is what I am doing.
First thing the site visitor needs to know is what the website is about. It’s about them, and how they can lose weight effectively. It’s only secondarily about me, and the w
ebsite must talk about me only from the point of view of how can I help them. It is your job to create a webpage where I can do just that. I have the content of this page ready to go, but I need you to create a beautiful, enticing, and effective framework to put it all in. You do not need to enter any copy except for the small amount noted below.
My clients are looking for a weight loss method or program that is effective, healthy, and long-lasting. This system addresses those needs. It's important for the clients to know that with the lumivaleYOU system, there is no hunger, no deprivation, no pills, no weighing foods or calorie counting, no special products to buy, among other things.
And not only does the weight come off, but there are other health benefits as well. The lumivaleYOU system can lower cholesterol, blood pressure, dependence on insulin for type 2 diabetics, reduce risk of heart disease and certain types of cancer, among other things-and this has been medically documented.
When I say "healthy eating", the focus of this program is on vegetables, fruits, and grains, with no added fat, but I do not want the main page to highlight that, since the whole notion of lots of veggies can scare people away. Pictures of fruits and veggies are fine. I'll introduce scary words like “vegan” and “no added fat” into the written materials and in the video, but there is no point in chasing people away too quickly!
The banner headline should have incorporated into it, in addition to the business name, the following: "Lose weight...improve your looks...improve your health...transform your life". You will need to choose a typeface and add this copy.
I would like to have a collage of healthy, happy, slender people of all ages (mostly women), in group and social settings-but not all exercising or doing yoga or jogging, since many of my target audience are couch potatoes (at least right now). If you do use any pictures of overweight people, they should be solitary, not part of a group, and definitely not looking happy!. I was thinking of having this only in the banner at top, but if you find a way to make the site attractive by adding a thin border with this as well, feel free.
Or, since I am not a design person by any stretch of the imagination, if you have another idea as to the banner design and the rest, I am certainly open to it.
In addition to the banner headline, I want a two-column design on the lower section, one being a narrower sidebar on the right, with a place for the customer to enter his/her name, and the following: Free video & eBook" "Why Meal Plans Fail, Keep Failing, And Always Will Fail-And How To Break Free Of Them", and they get this in exchange for entering their first and last name, and email address. I can link this to Quillpost later. I have a video widget, as well as a bunch more, in place, so you do not need to create or order those.
I will later add something to this section about no spam will be sent.
Below that in the same thinner column on the right should be an archives section, which you will need to create if the Wordpress theme doesn't have it already. This should be the same on all pages, except the single column pages, and since they will have sales pitches, should not have anything else.
The wider, main column I want to have three particular areas: One, is video. Two is text. Three is comments.
I will be using a LOT of video, but below each video I want to be able to place the text for the video (not everyone wants to watch a video), I want a static first page, but no comments section on the first page (I may want to add a comments section later, but not now).
The next page will be a basic "about me" page. This will be a video with text below in the main section, and will have the same enter your email info on the right side bar. No need to have "comments" below this. I've uploaded a picture of me, which should appear on this page, as well as on the main page.
Then will be a blog page, again the same layout: videos, which I can add to consecutively, with "comments" below, (which I can approve or disapprove before they get posted), with the offer in the right sidebar. Any videos will also show up in the archives section.
And a "recipes" page, video and text, plus comments section, with the email offer in the sidebar. These will show up as an archives section as well. I’ll add recipes and cooking videos later.
Then will be a "Products" page, which will for now be blank (I haven't created them yet), but with the email offer in the right side bar. No comments section to this one.
And a Contact Us page, no comments section either. I'll add the contact information later.
Across bottom of each page, perhaps in a somewhat contrasting color, will be a disclaimer, which I’ll need to be able to edit. This will be in small print, and should say something like, “This website expresses the opinions of the author, is intended for informational and educational purposes only, should not be construed as medical or dietary advice, and is not intended to be a substitute for same. Before changing diets, medications, or before undertaking a weight loss regimen, be sure to consult with your physician. This information is not intended to diagnose or treat any illness or health problems you may be experiencing, so kindly address your doctor with these concerns.” You can copy and paste this text.
Each page should also say “copyright 2014, Ned Porski”, which you will need to add.
Beyond that I will need single blank column pages which I will later make into landing, thank you, and so on pages. This will not be visible from the main page, though.

This will be done in Wordpress. I have the URL and the page is set up on Wordpress already, but I will need you to integrate the design into my Wordpress site when it is completed, so you will need a working knowledge of Wordpress. So the final winner will need to have the capability of coding the design and uploading it into my website and server. When you are done, it will be a complete and turnkey website, and all I have to do is add the copy and videos.

I am not particular as to a Wordpress theme, as long as it's an unpaid one, but if you find a paid one that you think is useable and needs to be paid for, let me know so I can check it out.
And I will need to be easily able to change and edit anything in the webpage on Wordpress at the end, after you are finished, with NO HTML, so any theme must be dummy friendly (I am the dummy, by the way!). (I have a basic familiarity with Wordpress, but none of HTML.)

Hopefully this gives you more than enough information to work with. Even though this page is a bit complicated, the actual website should be pretty simple looking, not busy or full of distractions, with only a few focal points.
Updates

Hi-information has been updated, I've changed my status to "committed", and I've uploaded a lot of pictures of fruit and veggies for you to use.  Thanks for your attention!
Ned

Target Market(s)

As stated above, "The target audience is 80% women, of all races and ethnic backgrounds, in the 35-55 age range, all of whom are overweight and want to lose weight."

Industry/Entity Type

Cooking

Font styles to use
Serif

Requirements
Must have
• The home page serves two purposes: one, to introduce the reader to the material, but two, and equally important, to build my email list. To that end, the opt in form on the right should say prominently, Free video & eBook" "Why Meal Plans Fail, Keep Failing, And Always Will Fail-And How To Break Free Of Them", and below that should be the opt in boxes.
The banner can be scrolling, to attract ATTENTION, should lead to the ACTION of watching the video, which will have in it a CALL TO ACTION of signing up for the hopefully compelling OFFER of the free ebook and video-and of course the newsletter. My purpose on page one is to directly address the question of "What's in it for me?", and then to deliver with the video and ebook offer.
I've uploaded a bunch of pictures of veggies and fruit-feel free to use them, as they are all mine.
Possibly a scrolling banner could be used with alternating pictures of happy, slender people alternating with pictures, and the captions of "lLose weight...improve your looks...improve your health...transform your life"

Emphasis should be on healthy eating, not on pounds lost or measuring one's waist or some such thing.

Banner headline should include: ""Lose weight...improve your looks...improve your health...transform your life"
Nice to have
Should not have
• Please avoid pictures of picture-perfect people, scales, and so on-I do not want this to be some generic, cookie-cutter weight loss web site. This is about weight loss from a different point of view-and I don't think this will come across in the webpage, but the concept will be introduced later. It's about weight loss as a byproduct of changing eating habits from unhealthy to healthy.

```html
<!DOCTYPE html>
<html lang="en">
<head>
<meta charset="utf-8">
<title>Lumivale You</title>
<link rel="stylesheet" href="https://fonts.googleapis.com/css2?family=Open+Sans:wght@400;600&display=swap">
<style>
:root{
  --green:#6e8b03;
  --green-dark:#56700a;
  --field:#5a7403;
  --grey-box:#9c9c9c;
  --panel:#e2e2e2;
  --text:#8a8a8a;
  --title:#555;
  --accent:#d6362b;
  --white:#fff;
}
*{margin:0;padding:0;box-sizing:border-box}
html,body{width:758px;height:1200px;overflow:hidden;background:var(--white)}
body{position:relative;font-family:"Open Sans",Arial,sans-serif;color:var(--text)}
.abs{position:absolute}
.visually-hidden{position:absolute;width:1px;height:1px;overflow:hidden;clip:rect(0 0 0 0);white-space:nowrap}
.site-header{left:0;top:0;width:758px;height:62px;background:var(--green)}
.brand{left:64px;top:16px;font-size:22px;color:var(--white);font-weight:400}
.main-nav{left:0;top:0;width:758px;height:62px}
.main-nav span{position:absolute;top:26px;font-size:9px;color:var(--white);white-space:nowrap}
.search{left:572px;top:23px;width:123px;height:17px;background:var(--field);border:1px solid #4f6600}
.search-btn{right:0;top:0;width:18px;height:15px;background:#3f5200}
.hero{left:0;top:62px;width:758px;height:340px;background:#fbfbfb}
.hero-fruit{left:64px;top:0;width:640px;height:340px;background:radial-gradient(circle at 35% 35%,#ffb23a 0,#f7d04d 30%,#f3f3ec 70%)}
.hero-person{left:440px;top:0;width:244px;height:340px;background:linear-gradient(180deg,#f2f2f2 0,#e7c9b2 30%,#2f4f86 55%,#233f70 100%)}
.hero-arrow{top:223px;width:24px;height:24px;border-radius:50%}
.caption{left:64px;width:289px;height:28px;background:rgba(110,139,3,.85);color:var(--white);font-size:15px;line-height:28px;padding-left:14px;white-space:nowrap}
.dots{left:360px;top:328px;display:flex;gap:5px}
.dots span{width:5px;height:5px;border-radius:50%;background:#ccc}
.dots span:first-child{background:var(--green)}
.post-img{left:64px;width:211px;height:151px}
.date{left:289px;width:69px;height:70px;color:var(--white);box-shadow:2px 2px 3px rgba(0,0,0,.25)}
.date b{position:absolute;left:10px;font-weight:400;font-size:17px}
.date i{position:absolute;left:31px;font-style:normal;font-size:5.5px}
.post-title{left:370px;width:122px;font-size:13px;line-height:15px;color:var(--title);font-weight:400;letter-spacing:-.2px}
.meta{left:370px;font-size:5.5px;color:#777;white-space:nowrap}
.meta em{font-style:normal;color:var(--accent)}
.excerpt{left:288px;width:200px;font-size:7.6px;line-height:13.4px;text-align:justify;color:var(--text)}
.page{width:20px;height:20px;border-radius:50%;background:#d9d9d9;color:#666;font-size:8px;text-align:center;line-height:20px;top:1007px}
.page.on{background:var(--green);color:var(--white)}
.optin{left:497px;top:432px;width:198px;height:198px;background:var(--green);color:var(--white);text-align:center}
.optin h2{font-weight:400;font-size:15.5px;margin-top:9px}
.optin p{font-size:7.6px;line-height:12.5px;margin:4px 10px 0}
.field{left:41px;width:117px;height:18px;background:var(--field);font-size:8px;line-height:18px;text-align:left;padding-left:8px}
.submit{left:41px;top:155px;width:117px;height:22px;background:linear-gradient(#435500,#2c3a00);font-size:8px;font-weight:600;line-height:22px}
.arch-head{left:497px;top:648px;width:198px;height:27px;background:var(--green);color:var(--white);font-size:15.5px;text-align:center;line-height:27px}
.arch-list{left:497px;top:675px;width:198px;height:253px;background:var(--panel);list-style:none;padding:18px 0 0 27px}
.arch-list li{font-size:8.8px;color:#555;height:19.1px;position:relative;padding-left:12px;white-space:nowrap}
.arch-list li::before{content:"";position:absolute;left:-3px;top:4px;width:5px;height:5px;border-radius:50%;background:#b3b3b3}
.site-footer{left:0;top:1075px;width:758px;height:125px;background:var(--green)}
.foot-links{left:64px;top:12px;font-size:7.8px;color:#d9e3a6}
.copy{left:64px;top:27px;font-size:7.8px;color:#d9e3a6}
.copy strong{color:var(--white);font-weight:400}
.social{top:14px;width:19px;height:19px;border-radius:50%;background:var(--white)}
.disclaimer{left:64px;top:47px;width:631px;height:66px;background:var(--green-dark);color:#e8edd5;font-size:7.8px;line-height:12px;text-align:center;padding:9px 12px}
</style>
</head>
<body>
<header class="site-header abs">
  <div class="brand abs">Lumivale You</div>
  <nav class="main-nav abs">
    <span style="left:279px">Home</span>
    <span style="left:323px">About me</span>
    <span style="left:381px">Blog</span>
    <span style="left:418px">Recipes</span>
    <span style="left:469px">Products</span>
    <span style="left:522px">Contact us</span>
  </nav>
  <div class="search abs">
    <div class="search-btn abs"><svg width="18" height="15" viewBox="0 0 18 15"><circle cx="8.5" cy="6.5" r="3" fill="none" stroke="#fff" stroke-width="1.2"/><line x1="10.6" y1="8.6" x2="12.5" y2="10.5" stroke="#fff" stroke-width="1.4"/></svg></div>
  </div>
</header>

<section class="hero abs">
  <h1 class="visually-hidden">Lumivale You: Lose weight...improve your looks...improve your health...transform your life</h1>
  <div class="hero-fruit abs" role="img" aria-label="Halved oranges, lemons, kiwi and strawberries"></div>
  <div class="hero-person abs" role="img" aria-label="Smiling author in a blue sweater"></div>
  <svg class="hero-arrow abs" style="left:12px" viewBox="0 0 24 24"><circle cx="12" cy="12" r="12" fill="#7d9a12"/><path d="M14 7l-5 5 5 5" fill="none" stroke="#fff" stroke-width="2.5"/></svg>
  <svg class="hero-arrow abs" style="left:720px" viewBox="0 0 24 24"><circle cx="12" cy="12" r="12" fill="#e3e3e3"/><path d="M10 7l5 5-5 5" fill="none" stroke="#fff" stroke-width="2.5"/></svg>
  <div class="caption abs" style="top:212px">No hunger, No deprivation, No pills</div>
  <div class="caption abs" style="top:251px">No weighing foods or Calorie counting</div>
  <div class="dots abs"><span></span><span></span><span></span></div>
</section>

<article>
  <div class="post-img abs" style="top:441px;background:linear-gradient(135deg,#e9e4de,#9fd3e6 50%,#3a3a3a)" role="img" aria-label="Video still of a woman measuring her waist by a pool"></div>
  <svg class="abs" style="left:158px;top:498px" width="30" height="30" viewBox="0 0 30 30"><rect width="30" height="30" rx="3" fill="#6e8b03"/><path d="M11 8l11 7-11 7z" fill="#fff"/></svg>
  <div class="date abs" style="top:440px;background:var(--green)"><b style="top:6px">16</b><i style="top:14px">Feb 2013</i><b style="top:43px">45</b><i style="top:52px">Comments</i></div>
  <h3 class="post-title abs" style="top:439px">Whoops....wrong neighborhood.</h3>
  <div class="meta abs" style="top:474px">Posted by <em>admin</em> // in <em>Awesomeness</em></div>
  <p class="excerpt abs" style="top:518px">He further the spiritual evolution of mankind has advanced, the more certaint seems to me that the path to genuine religiosity does not lie through the. simply dummy text of the printing and typesetting industry. Lorem Ipsum has been the industry's standard dummy text ever since the 1500s.</p>
</article>

<article>
  <div class="post-img abs" style="top:631px;background:linear-gradient(135deg,#d9c0a8,#c9a88e 50%,#4a6a8c)" role="img" aria-label="Tape measure around a waist"></div>
  <div class="date abs" style="top:630px;background:var(--grey-box)"><b style="top:6px">16</b><i style="top:14px">Feb 2013</i><b style="top:43px">45</b><i style="top:52px">Comments</i></div>
  <h3 class="post-title abs" style="top:629px">Lorem ipsum contnt dolor</h3>
  <div class="meta abs" style="top:664px">Posted by <em>admin</em> // in <em>Awesomeness</em></div>
  <p class="excerpt abs" style="top:708px">He further the spiritual evolution of mankind has advanced, the more certaint seems to me that the path to genuine religiosity does not lie through the. simply dummy text of the printing and typesetting industry. Lorem Ipsum has been the industry's standard dummy text ever since the 1500s.</p>
</article>

<article>
  <div class="post-img abs" style="top:827px;background:linear-gradient(160deg,#8bb21a,#a8c34a 45%,#c08a4a)" role="img" aria-label="Bare feet on a bathroom scale"></div>
  <div class="date abs" style="top:826px;background:var(--grey-box)"><b style="top:6px">16</b><i style="top:14px">Feb 2013</i><b style="top:43px">45</b><i style="top:52px">Comments</i></div>
  <h3 class="post-title abs" style="top:825px">Lorem ipsum contnt dolor</h3>
  <div class="meta abs" style="top:860px">Posted by <em>admin</em> // in <em>Awesomeness</em></div>
  <p class="excerpt abs" style="top:904px">He further the spiritual evolution of mankind has advanced, the more certaint seems to me that the path to genuine religiosity does not lie through the. simply dummy text of the printing and typesetting industry. Lorem Ipsum has been the industry's standard dummy text ever since the 1500s.</p>
</article>

<div class="page on abs" style="left:241px">1</div>
<div class="page abs" style="left:267px">2</div>
<div class="page abs" style="left:292px">3</div>

<aside>
  <form class="optin abs">
    <h2>Free E-Book &amp; Videos</h2>
    <p>Why Meal Plans Fail, Keep Failing, And Always Will Fail-And How To Break Free Of Them</p>
    <div class="field abs" style="top:71px">First Name</div>
    <div class="field abs" style="top:97px">Last Name</div>
    <div class="field abs" style="top:123px">Enter Your Email Id</div>
    <div class="submit abs">SUBMIT</div>
  </form>
  <div class="arch-head abs">Archives</div>
  <ul class="arch-list abs">
    <li>Established fact that a reader</li>
    <li>will be Distracted by the read-</li>
    <li>able content of a Page when</li>
    <li>looking at its layout. The Pointf</li>
    <li>using Lorem Ipsum is that it has</li>
    <li>More-or-less normal distribu-</li>
    <li>tion of Letters, as opposed to</li>
    <li>using 'Content here, content</li>
    <li>here', making it look like read-</li>
    <li>able English. Many desktop</li>
    <li>publishing packages and web</li>
  </ul>
</aside>

<footer class="site-footer abs">
  <div class="foot-links abs">Home &nbsp;/&nbsp; Work &nbsp;/&nbsp; Careers &nbsp;/&nbsp; Experience &nbsp;/&nbsp; Company</div>
  <div class="copy abs">Copyright © 2014 <strong>Ned Porski</strong> , All Rights Reserved.</div>
  <div class="social abs" style="left:596px"></div>
  <div class="social abs" style="left:623px"></div>
  <div class="social abs" style="left:649px"></div>
  <div class="social abs" style="left:676px"></div>
  <p class="disclaimer abs">This website expresses the opinions of the author, is intended for informational and educational purposes only, should not be construed as medical or dietary advice, and is not intended to be a substitute for same. Before changing diets, medications, or before undertaking a weight loss regimen, be sure to consult with your physician. This information is not intended to diagnose or treat any illness or health problems you may be experiencing, so kindly address your doctor with these concerns</p>
</footer>
</body>
</html>
```